Business Card Design Project for Heron Lending

Hello there,

We are looking for a business card design for our new Heron Lending car financing company. We are looking for a business card that will include:

- An address
- Telephone number and extension
- Employee Name
- Employee Title
- Our logo and name clearly visible

We are including our logo with this writeup, we are looking to convey friendliness, trus and memorability. Colors and everything else is up to you.

Target Market(s)

18-34 year old males and females

Industry/Entity Type

Business

```html
<!DOCTYPE html>
<html lang="en">
<head>
<meta charset="utf-8">
<title>Heron Lending — Business Cards</title>
<link rel="stylesheet" href="https://fonts.googleapis.com/css2?family=Noto+Serif:wght@400;700&display=swap">
<style>
  :root {
    --bg: #e9e6e1;
    --card: #ffffff;
    --ink: #1b1d22;
    --navy: #22346b;
    --muted: #4a4d55;
    --rule: #9a9a9a;
    --shadow: rgba(40, 30, 15, 0.22);
  }
  * { box-sizing: border-box; margin: 0; padding: 0; }
  html, body { width: 1200px; height: 800px; overflow: hidden; }
  body {
    background: var(--bg);
    font-family: "Noto Serif", Georgia, serif;
    color: var(--ink);
    position: relative;
  }
  .card {
    position: absolute;
    width: 520px;
    height: 300px;
    background: var(--card);
    box-shadow: 0 10px 26px var(--shadow), 0 2px 4px rgba(0,0,0,0.12);
    overflow: hidden;
  }
  .card--front { left: 50px; top: 90px; }
  .card--back  { left: 630px; top: 410px; }

  .brand {
    display: flex;
    align-items: center;
    gap: 12px;
  }
  .brand__dot {
    width: 16px; height: 16px;
    border-radius: 50%;
    background: var(--navy);
  }
  .brand__name {
    font-weight: 400;
    font-size: 30px;
    letter-spacing: 0.08em;
    color: var(--navy);
    line-height: 1;
  }
  .card--front .brand {
    position: absolute; inset: 0;
    justify-content: center;
  }

  .card--back .contact {
    position: absolute;
    left: 190px; right: 20px; top: 20px;
  }
  .contact__name { font-size: 18px; font-weight: 700; line-height: 1.15; }
  .contact__title { font-size: 9.5px; line-height: 1.3; color: var(--muted); margin-bottom: 10px; }
  .contact__list { list-style: none; font-size: 11.5px; color: var(--ink); }
  .contact__list li { display: flex; align-items: flex-start; gap: 10px; line-height: 1.3; margin-bottom: 3px; }
  .contact__list li:last-child { margin-bottom: 0; }
  .contact__list svg { width: 12px; height: 12px; flex: none; margin-top: 2px; fill: var(--navy); }

  .divider {
    position: absolute;
    left: 0; right: 60px; top: 168px;
    height: 1px;
    background: linear-gradient(90deg, rgba(154,154,154,0.15), var(--rule) 30%, var(--rule) 70%, rgba(154,154,154,0.1));
  }
  .card--back .brand {
    position: absolute;
    left: 0; right: 0; top: 169px; bottom: 0;
    justify-content: center;
  }
</style>
</head>
<body>

  <section class="card card--front" aria-label="Card front">
    <div class="brand">
      <span class="brand__dot"></span>
      <span class="brand__name">HERON LENDING</span>
    </div>
  </section>

  <section class="card card--back" aria-label="Card back">
    <div class="contact">
      <p class="contact__name">Employee Name</p>
      <p class="contact__title">Managing Director</p>
      <ul class="contact__list">
        <li>
          <svg viewBox="0 0 12 12" aria-hidden="true"><path d="M2.5 1 4.5 1 5.2 3.6 4 4.6C4.6 6 5.9 7.3 7.4 8L8.4 6.8 11 7.5V9.5C11 10.3 10.3 11 9.5 11 5 11 1 7 1 2.5 1 1.7 1.7 1 2.5 1Z"/></svg>
          <span>0047 2861 530 &middot; ext. 214</span>
        </li>
        <li>
          <svg viewBox="0 0 12 12" aria-hidden="true"><path d="M1 2.5h10v7H1z M1.6 3 6 6.6 10.4 3" stroke="#fff" stroke-width="0.8"/></svg>
          <span>hello@heronlending.co</span>
        </li>
        <li>
          <svg viewBox="0 0 12 12" aria-hidden="true"><circle cx="6" cy="6" r="5"/><path d="M1 6h10M6 1c-2.4 2.8-2.4 7.2 0 10M6 1c2.4 2.8 2.4 7.2 0 10" stroke="#fff" stroke-width="0.7" fill="none"/></svg>
          <span>www.heronlending.co</span>
        </li>
        <li>
          <svg viewBox="0 0 12 12" aria-hidden="true"><path d="M6 0.8C3.9 0.8 2.3 2.4 2.3 4.5 2.3 7.3 6 11.2 6 11.2S9.7 7.3 9.7 4.5C9.7 2.4 8.1 0.8 6 0.8Zm0 5.1A1.4 1.4 0 1 1 6 3.1 1.4 1.4 0 0 1 6 5.9Z"/></svg>
          <span>Suite 12, 48 Alder Row<br>Brookfield, ST 00000</span>
        </li>
      </ul>
    </div>
    <div class="divider"></div>
    <div class="brand">
      <span class="brand__dot"></span>
      <span class="brand__name">HERON LENDING</span>
    </div>
  </section>

</body>
</html>
```